LearnNest Business Cards

I will be teaching Zorvo and Kelvix classes to the 55+community.Small groups of 10(max), or individual lessons.Beginner and Advance ClassesTraining Material ProvidedThis is a new business in Florida.I hope to order business cards and brochures.I found sample of business card on Printobel - see below. I like the looks of this card, instead of a lighthouseI would like an apple with the red and white stripes. The red and white apple will be my logo. Thank you,Marla Quenby
Target Market(s)
55+ Adults
Industry/Entity Type
Business
Contact Information for Business Card
Marla ApplebyOwner/Instructor772 571-7011iteachdiane@gmail.com
Look and feel
Each slider illustrates characteristics of the customer's brand and the style your logo design should communicate.

```html
<!DOCTYPE html>
<html lang="en">
<head>
<meta charset="utf-8">
<title>LearnNest Business Card</title>
<link href="https://fonts.googleapis.com/css2?family=Lato:wght@400;700&family=Arimo&display=swap" rel="stylesheet">
<style>
  :root {
    --stage: #000000;
    --paper: #ffffff;
    --brand-red: #d70000;
    --back-red: #c80404;
    --edge-pink: #e8638a;
    --edge-dark: #b00010;
    --ink-light: #ffffff;
    --mark-light: #f3e6e6;
  }
  * { margin: 0; padding: 0; box-sizing: border-box; }
  html, body {
    width: 1200px; height: 864px; overflow: hidden;
    background: var(--stage);
  }
  .canvas { position: relative; width: 1200px; height: 864px; }
  .card { position: absolute; overflow: hidden; }
  .card-front {
    left: 329px; top: 86px; width: 542px; height: 317px;
    background: var(--paper);
  }
  .card-back {
    left: 327px; top: 447px; width: 542px; height: 320px;
    background: var(--back-red);
  }
  .front-shape { position: absolute; inset: 0; }
  .brand-name {
    position: absolute;
    font-family: "Lato", sans-serif;
    font-weight: 700;
    white-space: nowrap;
    transform: translate(-50%, -50%);
  }
  .card-front .brand-name {
    left: 131px; top: 159px; font-size: 32px; color: var(--brand-red);
  }
  .card-back .brand-name {
    left: 271px; top: 158px; font-size: 46px; color: var(--mark-light);
  }
  .details {
    position: absolute; left: 298px; top: 62px;
    color: var(--ink-light);
  }
  .person-name {
    font-family: "Lato", sans-serif; font-weight: 700;
    font-size: 28px; line-height: 32px;
  }
  .person-role {
    font-family: "Lato", sans-serif; font-weight: 400;
    font-size: 16px; line-height: 20px;
  }
  .contact-list {
    list-style: none; margin-top: 23px;
    font-family: "Arimo", Arial, sans-serif; font-size: 14.5px;
  }
  .contact-list li {
    display: flex; align-items: flex-start;
    line-height: 17px; margin-bottom: 6px;
  }
  .contact-list svg {
    width: 10px; height: 10px; margin: 4px 6px 0 0; flex: none;
    fill: var(--ink-light);
  }
</style>
</head>
<body>
<main class="canvas">
  <section class="card card-front" aria-label="Business card front">
    <svg class="front-shape" viewBox="0 0 542 317" aria-hidden="true">
      <path d="M286 40 Q200 190 282 317 L300 317 Q230 180 293 0 Z" fill="var(--edge-pink)"/>
      <path d="M293 0 Q187 160 293 317 L542 317 L542 0 Z" fill="var(--edge-dark)"/>
      <path d="M296 0 Q192 160 296 317 L542 317 L542 0 Z" fill="var(--brand-red)"/>
    </svg>
    <span class="brand-name">LearnNest</span>
    <div class="details">
      <h1 class="person-name">Arlo Penwick</h1>
      <p class="person-role">Managing Director</p>
      <ul class="contact-list">
        <li><svg viewBox="0 0 10 10"><path d="M1 3 Q5 0 9 3 L8 5 L6 4 L6 3 Q5 2.6 4 3 L4 4 L2 5 Z M2 6 L8 6 L8 9 L2 9 Z"/></svg>046-318 720 594</li>
        <li><svg viewBox="0 0 10 10"><path d="M3 0 H7 V10 H3 Z M4 1 V8 H6 V1 Z"/></svg>046-318 720 594</li>
        <li><svg viewBox="0 0 10 10"><path d="M0 2 H10 V8 H0 Z M1 3 L5 6 L9 3 Z" fill-rule="evenodd"/></svg>info@mailvero.com</li>
        <li><svg viewBox="0 0 10 10"><path d="M2 9 L0 7 L4 3 L5 4 L2 7 L3 8 L6 5 L7 6 Z M6 5 L5 4 L8 1 L7 0 L4 3 L3 2 L7 -1 L10 1 Z"/></svg>www.pagelume.com</li>
        <li><svg viewBox="0 0 10 10"><path d="M5 0 A3.5 3.5 0 0 1 8.5 3.5 C8.5 6 5 10 5 10 C5 10 1.5 6 1.5 3.5 A3.5 3.5 0 0 1 5 0 Z M5 2 A1.5 1.5 0 1 0 5 5 A1.5 1.5 0 1 0 5 2 Z" fill-rule="evenodd"/></svg>12345, Address Goes Here<br>Country Name, 123456</li>
      </ul>
    </div>
  </section>

  <section class="card card-back" aria-label="Business card back">
    <span class="brand-name">LearnNest</span>
  </section>
</main>
</body>
</html>
```